4x6 postcard design Tide And Time

A full color double sided postcard 4x6 postcard. I have attached a screenshot of the text that should be used on the postcard. The front is titled this is the front. The back is titled the back. REMEMBER THE screenshots are used to show you the text. Please design using your own creative methods. The color scheme should remain pretty similar to the screenshot.

On the front of the card, I'd like to add a 4th bullet (or check) that says This is NOT cash gifting!
Also on the front, add a line that says call 877-402-3915 or send an email to join@tideandtimeco.net and mention ID#:

On the back, please add a line that says call 877-402-3915 or send an email to join@tideandtimeco.net and mention ID#:

On the front OR back it should say 100% Satisfaction Guarantee

Target Market(s)

work from home

Font styles to use
Sans Serif

Requirements
Must have
• The correct text on both sides. Please read the directions carefully.
Nice to have
• A very creative, attention-grabbing design. The 100% Satisfaction Guarantee designed in a way that looks like the gold seals that pop up if you google "money back guarantee seal"

```html
<!DOCTYPE html>
<html lang="en">
<head>
<meta charset="utf-8">
<title>Tide And Time – Postcard</title>
<link href="https://fonts.googleapis.com/css2?family=Roboto:ital,wght@0,300;0,400;0,700;0,900;1,700;1,900&family=Roboto+Condensed:wght@700&display=swap" rel="stylesheet">
<style>
  :root{
    --stage:#cdd0d3;
    --paper:#ffffff;
    --ink:#111111;
    --orange:#f39a3a;
    --orange-band:#f7963a;
    --gold:#f2c04a;
    --gold-dark:#c9922a;
    --green:#0b7a3e;
    --green-soft:#1f9a4d;
    --red:#e0202a;
    --stamp:#fdf6ea;
    --rule:#9a9a9a;
    --pill:#d4d4d4;
  }
  *{box-sizing:border-box;margin:0;padding:0}
  html,body{width:1200px;height:1200px;overflow:hidden}
  body{background:var(--stage);font-family:"Roboto",Arial,sans-serif;color:var(--ink);position:relative}
  .card{position:absolute;background:var(--paper);overflow:hidden}
  .abs{position:absolute}

  /* ---------- Back side ---------- */
  .card-back{left:54px;top:26px;width:710px;height:550px}
  .back-title{left:47px;top:36px;font-size:30px;font-weight:700;color:var(--orange);white-space:nowrap}
  .back-intro{left:47px;top:77px;width:480px;font-size:17.5px;font-weight:300;line-height:21px}
  .steps-heading{left:47px;top:142px;font-size:22px;font-weight:700;white-space:nowrap}
  .steps-heading em{font-size:16px;font-weight:900;font-style:italic}
  .steps-bracket{left:31px;top:156px;width:12px;height:144px;border-left:1.5px solid var(--ink);border-top:1.5px solid var(--ink);border-bottom:1.5px solid var(--ink)}
  .step{left:43px;display:flex;align-items:flex-start;gap:12px;font-size:13.6px;font-weight:300;line-height:17px}
  .step-num{position:relative;flex:none;width:24px;height:24px;border-radius:50%;background:var(--gold);font-weight:700;font-size:13px;display:flex;align-items:center;justify-content:center;margin-top:-4px}
  .step-num::before{content:"";position:absolute;left:-12px;top:11px;width:12px;border-top:1.5px solid var(--ink)}
  .step-1{top:184px}
  .step-2{top:218px;width:320px}
  .step-3{top:286px;width:320px}
  .cash-note{left:34px;top:326px;font-family:"Roboto Condensed",Arial,sans-serif;font-weight:700;font-size:14px;line-height:17px}
  .back-cta{left:0;top:372px;width:343px;height:82px;background:var(--orange-band);padding:4px 0 0 32px;font-weight:700;line-height:18px;font-size:14.5px}
  .back-cta .phone{font-size:29px;line-height:32px;white-space:nowrap}
  .back-cta .phone small{font-size:14px}
  .stamp-box{left:543px;top:34px;width:139px;height:131px;background:var(--stamp)}
  .address-line{left:426px;width:257px;border-top:1px solid var(--rule)}
  .guarantee{left:540px;top:458px;width:84px;height:84px;border-radius:50%;
    background:radial-gradient(circle,#ffe27a 0%,var(--gold) 60%,var(--gold-dark) 100%);
    border:3px double #8a5f12;display:flex;flex-direction:column;align-items:center;justify-content:center;
    text-align:center;color:#3a2a05;font-weight:900;line-height:1}
  .guarantee .pct{font-size:22px}
  .guarantee .txt{font-size:8px;font-weight:700;margin-top:3px;letter-spacing:.3px}

  /* ---------- Front side ---------- */
  .card-front{left:436px;top:597px;width:746px;height:578px}
  .photo-area{left:300px;top:200px;width:446px;height:378px;
    background:radial-gradient(ellipse 60% 60% at 62% 52%, #f3d660 0%, #f1dd8e 35%, #f6ead0 60%, rgba(255,255,255,0) 100%)}
  .brand{left:52px;top:50px;width:180px;text-align:center}
  .brand-dot{display:block;margin:0 auto 8px;width:62px;height:62px;border-radius:50%;background:var(--gold)}
  .brand-name{font-size:22px;font-weight:700;color:var(--green);white-space:nowrap}
  .front-kicker{left:264px;top:36px;font-size:33px;font-weight:900;color:var(--green);white-space:nowrap;letter-spacing:.2px}
  .front-sub{left:264px;top:74px;font-size:18px;font-weight:400;white-space:nowrap}
  .front-sub-green{left:264px;top:95px;font-size:16px;font-weight:300;color:var(--green-soft);white-space:nowrap}
  .front-headline{left:260px;top:126px;color:var(--red);font-weight:900;line-height:.9}
  .front-headline .l1{display:block;font-size:36px}
  .front-headline .l2{display:block;font-size:47px}
  .benefit{left:46px;width:360px;border-radius:24px 0 0 24px;
    background:linear-gradient(90deg,var(--pill) 0%,rgba(212,212,212,.75) 55%,rgba(212,212,212,0) 100%);
    display:flex;align-items:center;padding-left:14px;gap:10px;font-weight:700;font-size:16.5px;line-height:19px}
  .benefit svg{flex:none}
  .b1{top:227px;height:44px}
  .b2{top:275px;height:43px}
  .b3{top:321px;height:45px}
  .b4{top:369px;height:44px}
  .signup{left:86px;top:422px;width:242px;height:41px;border-radius:21px;border:2px solid #3a2a05;
    background:linear-gradient(180deg,#fff36a 0%,#f6d21c 55%,#e8a915 100%);
    font-size:26px;font-weight:900;text-align:center;line-height:37px;letter-spacing:.3px}
  .front-call{left:62px;top:473px;font-weight:700;font-size:16px;line-height:19px}
  .front-call .phone{color:var(--red);font-size:32px;line-height:34px;white-space:nowrap}
  .front-call .phone small{color:var(--ink);font-size:16px}
</style>
</head>
<body>

<!-- Back side -->
<section class="card card-back">
  <h2 class="abs back-title">What is a courseware distributor?</h2>
  <p class="abs back-intro">A Courseware Distributor is someone such as yourself that joins Tide And Time, and earns thousands of dollars in cash commissions each week. All you have to do is follow</p>
  <p class="abs steps-heading">3 simple steps <em>to change your financial health forever:</em></p>
  <div class="abs steps-bracket"></div>
  <div class="abs step step-1"><span class="step-num">1</span><span>Call or email right away to join</span></div>
  <div class="abs step step-2"><span class="step-num">2</span><span>Allow our attention-grabbing postcards or sales letters to work for your to get sales while you sleep</span></div>
  <div class="abs step step-3"><span class="step-num">3</span><span>Sit back and let our trained professionals answer your call and close your sales</span></div>
  <p class="abs cash-note">Your CASH commission will arrive at<br>your door via Overnight Courier, 6 days per week</p>
  <div class="abs back-cta">
    <div class="phone">Call 877-402-3915 <small>or</small></div>
    <div>send an email to join@tideandtimeco.net<br>and mention ID#:</div>
  </div>
  <div class="abs stamp-box"></div>
  <div class="abs address-line" style="top:240px"></div>
  <div class="abs address-line" style="top:290px"></div>
  <div class="abs address-line" style="top:339px"></div>
  <div class="abs address-line" style="top:389px"></div>
  <div class="abs address-line" style="top:438px"></div>
  <div class="abs guarantee"><span class="pct">100%</span><span class="txt">SATISFACTION<br>GUARANTEE</span></div>
</section>

<!-- Front side -->
<section class="card card-front">
  <div class="abs photo-area" role="img" aria-label="Photo of a smiling mother in a yellow top working on a laptop with her young daughter hugging her shoulders"></div>

  <div class="abs brand">
    <span class="brand-dot"></span>
    <span class="brand-name">Tide And Time</span>
  </div>

  <h2 class="abs front-kicker">DON’T PROCRASTINATE</h2>
  <p class="abs front-sub">People just like you are averaging oer $30,000</p>
  <p class="abs front-sub-green">per month with our quick and easy system.</p>
  <h1 class="abs front-headline"><span class="l1">START EARNING</span><span class="l2">THOUSANDS</span></h1>

  <div class="abs benefit b1">
    <svg width="34" height="30" viewBox="0 0 34 30"><path d="M2 16 L12 27 L32 2 L12 19 Z" fill="var(--gold)" stroke="#222" stroke-width="2" stroke-linejoin="round"/></svg>
    <span>We close all your sales for you....<br>Earn money 24 hours a day!</span>
  </div>
  <div class="abs benefit b2">
    <svg width="34" height="30" viewBox="0 0 34 30"><path d="M2 16 L12 27 L32 2 L12 19 Z" fill="var(--gold)" stroke="#222" stroke-width="2" stroke-linejoin="round"/></svg>
    <span>Done-for-your Marketing System</span>
  </div>
  <div class="abs benefit b3">
    <svg width="34" height="30" viewBox="0 0 34 30"><path d="M2 16 L12 27 L32 2 L12 19 Z" fill="var(--gold)" stroke="#222" stroke-width="2" stroke-linejoin="round"/></svg>
    <span>Real Producets pay “Gigantic”<br>cash commissions!</span>
  </div>
  <div class="abs benefit b4">
    <svg width="34" height="30" viewBox="0 0 34 30"><path d="M2 16 L12 27 L32 2 L12 19 Z" fill="var(--gold)" stroke="#222" stroke-width="2" stroke-linejoin="round"/></svg>
    <span>This is NOT cash gifting!</span>
  </div>

  <div class="abs signup">SING UP NOW</div>

  <div class="abs front-call">
    <div class="phone">Call 877-402-3915 <small>or</small></div>
    <div>send an email to join@tideandtimeco.net<br>and mention ID#:</div>
  </div>
</section>

</body>
</html>
```